Bright Meadow Party Coaches is excited to bring you Fenwick Valley’s Prime luxury limousine ser...

Leisure TransportationWedding DayWe will make your wedding day special and one to remember. Bright Meadow Party Coaches offers custom wedding transportation packages that are designed around your every need. Call our transportation consultant and learn how we can help you have a stress free and perfectly planned wedding event.PromsWe put safety first and give you piece of mind when we transport your loved ones.Special Occasions Bright Meadow Party Coaches professional chauffeured services will make any special event extraordinary. You will feel safe while our professional chauffeurs drive you in style and luxury.Corporate EventsNorth Coast Event Charters is a leader in professional chauffeured transportation services. Our highly trained staff will take the stress out of getting you to and from your destination. Bright Meadow Party Coaches is dedicated to the highest quality of services. Our top-of-the-line Calder-Voss Tramway is always safety inspected and cleaned before each use. Tours From the ocean to the redwoods, we offer tours to suit your needs.,Airport Service We are business ground travel experts. Our doo-to-door limousine can accommodate up to 10 passengers, and service all private and public airports

Target Market(s)

These brochures are going in motels and restaurants.

Font styles to use
Script

Colors
fed55c

Requirements
Must have
• Gold and black are the business colors. Check brand identity PDF

```html
<!DOCTYPE html>
<html lang="en">
<head>
<meta charset="utf-8">
<title>Bright Meadow Party Coaches – Brochure</title>
<link href="https://fonts.googleapis.com/css2?family=Cinzel:wght@400;600&family=Great+Vibes&family=Lato:wght@400;700&display=swap" rel="stylesheet">
<style>
  :root{
    --bg:#e4e4e4;
    --black:#0d0d0d;
    --charcoal:#1c1c1c;
    --gold:#c9a14a;
    --gold-bright:#fed55c;
    --paper:#ffffff;
    --ink:#3a3a3a;
    --muted:#8a8a8a;
  }
  *{box-sizing:border-box;margin:0;padding:0}
  html,body{width:800px;height:1200px;overflow:hidden;background:var(--bg)}
  body{position:relative;font-family:"Lato",sans-serif}
  .spread{position:absolute;left:90px;width:620px;height:440px;display:flex;box-shadow:0 8px 24px rgba(0,0,0,.18)}
  .spread--cover{top:80px}
  .spread--inside{top:660px}
  .page{position:relative;width:310px;height:440px;overflow:hidden}
  .photo{position:absolute}
  .curve{position:absolute;left:0;width:310px}

  /* back cover */
  .back-cover{background:var(--black)}
  .back-cover .photo{left:0;top:0;width:310px;height:230px;background:linear-gradient(160deg,#3b2f5c,#1a1a2a 55%,#5a4a3a)}
  .back-cover .curve{top:195px;height:70px}
  .back-cover__heading{position:absolute;left:0;width:100%;top:282px;text-align:center;font-family:"Cinzel",serif;font-size:9px;letter-spacing:1.5px;color:var(--gold)}
  .back-cover__text{position:absolute;left:40px;right:40px;top:300px;text-align:center;font-size:7px;line-height:1.5;color:#bdbdbd}
  .cta{position:absolute;left:75px;right:75px;top:340px;border:1px solid var(--gold);padding:7px 4px;text-align:center;font-family:"Cinzel",serif;font-size:8px;line-height:1.5;color:var(--gold-bright);letter-spacing:1px}
  .dots{position:absolute;top:395px;left:0;width:100%;display:flex;justify-content:center;gap:6px}
  .dots span{width:6px;height:6px;border-radius:50%;background:var(--gold)}

  /* front cover */
  .front-cover{background:var(--black)}
  .front-cover__top{position:absolute;left:0;top:0;width:100%;height:80px;background:var(--paper)}
  .brand{position:absolute;left:0;width:100%;top:22px;display:flex;align-items:center;justify-content:center;gap:8px;font-family:"Cinzel",serif;font-weight:600;font-size:10px;letter-spacing:1px;color:var(--black)}
  .brand__dot{width:22px;height:22px;border-radius:50%;background:var(--black)}
  .front-cover .photo{left:0;top:80px;width:310px;height:200px;background:linear-gradient(180deg,#9fb4a8,#5a6b5c 50%,#222 100%)}
  .front-cover .curve{top:250px;height:70px}
  .tagline{position:absolute;left:0;width:100%;top:335px;text-align:center;font-family:"Cinzel",serif;font-size:13px;letter-spacing:3px;color:var(--gold)}
  .tagline-script{position:absolute;left:0;width:100%;top:354px;text-align:center;font-family:"Great Vibes",cursive;font-size:18px;color:var(--gold-bright)}

  /* inside */
  .inside-left,.inside-right{background:var(--paper)}
  .section-title{position:absolute;left:30px;top:30px;font-family:"Cinzel",serif;font-size:14px;letter-spacing:2px;color:var(--ink)}
  .section-title em{font-style:normal;color:var(--gold)}
  .body-copy{position:absolute;font-size:7px;line-height:1.55;color:var(--ink)}
  .body-copy p+p{margin-top:6px}
  .inside-left .body-copy{left:30px;right:30px;top:56px}
  .inside-left .photo{left:0;top:200px;width:310px;height:170px;background:linear-gradient(180deg,#b7cbd6,#6f8f6a 45%,#3e4d36)}
  .inside-left .curve{top:345px;height:95px}
  .band-text{position:absolute;left:30px;bottom:18px;font-family:"Cinzel",serif;font-size:7px;letter-spacing:1.5px;color:var(--gold)}
  .inside-right .body-copy{left:30px;right:30px;top:30px}
  .inside-right .photo--van{left:0;top:140px;width:310px;height:150px;background:linear-gradient(180deg,#a9bfb0,#56684f 55%,#2a2a2a)}
  .inside-right .photo--guests{left:110px;top:285px;width:170px;height:120px;border:3px solid var(--paper);background:linear-gradient(150deg,#6b5a4a,#2e2a28);z-index:2}
  .inside-right .curve{top:330px;height:110px}
</style>
</head>
<body>

<section class="spread spread--cover">
  <article class="page back-cover">
    <div class="photo" role="img" aria-label="Guests celebrating inside a limousine with purple ceiling lights"></div>
    <svg class="curve" viewBox="0 0 310 70" preserveAspectRatio="none">
      <path d="M0 45 Q155 5 310 35 L310 70 L0 70 Z" fill="var(--black)"/>
      <path d="M0 40 Q155 0 310 30 L310 36 Q155 8 0 46 Z" fill="var(--gold)"/>
    </svg>
    <h3 class="back-cover__heading">EVENT TRANSPORTATION SPECIALISTS</h3>
    <p class="back-cover__text">Serving weddings, proms, tours and airport trips with care and style.</p>
    <p class="cta">BOOK YOUR EVENT TODAY!<br>CALL US AT 555-0142</p>
    <div class="dots"><span></span><span></span></div>
  </article>

  <article class="page front-cover">
    <div class="front-cover__top">
      <div class="brand"><span class="brand__dot"></span>Bright Meadow Party Coaches</div>
    </div>
    <div class="photo" role="img" aria-label="Black luxury van with a chauffeur standing at the open door"></div>
    <svg class="curve" viewBox="0 0 310 70" preserveAspectRatio="none">
      <path d="M0 40 Q150 0 310 30 L310 70 L0 70 Z" fill="var(--black)"/>
      <path d="M0 34 Q150 -6 310 24 L310 31 Q150 2 0 41 Z" fill="var(--gold)"/>
    </svg>
    <h1 class="tagline">LUXURY TRANSPORTATION</h1>
    <p class="tagline-script">for some of life’s biggest moments</p>
  </article>
</section>

<section class="spread spread--inside">
  <article class="page inside-left">
    <h2 class="section-title"><em>MISSION</em> STATEMENT</h2>
    <div class="body-copy">
      <p>Bright Meadow Party Coaches is excited to bring you Fenwick Valley’s Prime luxury limousine service. We put safety first and give you peace of mind on every ride.</p>
      <p>Our professional chauffeurs will make any special event extraordinary while you travel in style and comfort.</p>
    </div>
    <div class="photo" role="img" aria-label="Black van parked on a coastal road above the sea"></div>
    <svg class="curve" viewBox="0 0 310 95" preserveAspectRatio="none">
      <path d="M0 30 Q160 70 310 20 L310 95 L0 95 Z" fill="var(--black)"/>
      <path d="M0 24 Q160 64 310 14 L310 21 Q160 72 0 31 Z" fill="var(--gold)"/>
    </svg>
    <p class="band-text">BOOK YOUR EVENT TODAY · 555-0142</p>
  </article>

  <article class="page inside-right">
    <div class="body-copy">
      <p>Our top-of-the-line Calder-Voss Tramway is always safety inspected and cleaned before each use. From the ocean to the redwoods, we offer tours to suit your needs.</p>
      <p>We are ground travel experts for weddings, proms, corporate events and airport service.</p>
    </div>
    <div class="photo photo--van" role="img" aria-label="Black luxury van parked by green trees"></div>
    <svg class="curve" viewBox="0 0 310 110" preserveAspectRatio="none">
      <path d="M0 20 Q150 60 310 15 L310 110 L0 110 Z" fill="var(--black)"/>
      <path d="M0 14 Q150 54 310 9 L310 16 Q150 62 0 21 Z" fill="var(--gold)"/>
    </svg>
    <div class="photo photo--guests" role="img" aria-label="Prom guests posing beside a limousine"></div>
  </article>
</section>

</body>
</html>
```